Medical software helping patients with dry eye disease needs a business card

We have a logo we just need a design for a business card for a Canadian company called LUMA: Dry Eye. We use AI technology to assist optometrists in properly diagnosing patients with dry eye disease reducing wait times in doctors offices and accuracy of diagnosis as well as identifying key possible indicators and tailored treatment plans. The final design should be clean and medical looking. Our mission is to help patients and our logo using blues and whites.

```html
<!DOCTYPE html>
<html lang="en">
<head>
<meta charset="utf-8">
<title>LUMA: Dry Eye — Business Card</title>
<link href="https://fonts.googleapis.com/css2?family=Montserrat:wght@600;700&family=Open+Sans:wght@400;600&display=swap" rel="stylesheet">
<style>
  :root {
    --stage: #c9c9c9;
    --card-dark: #1d1d1e;
    --card-dark-soft: #262627;
    --brand-blue: #22a6e3;
    --paper-white: #ffffff;
    --text-light: #f2f2f2;
    --text-muted: #d8d8d8;
  }
  * { box-sizing: border-box; margin: 0; padding: 0; }
  html, body {
    width: 1200px; height: 788px; overflow: hidden;
    background: var(--stage);
    font-family: "Open Sans", Arial, sans-serif;
  }
  .stage {
    width: 1200px; height: 788px;
    display: flex; align-items: center; justify-content: center; gap: 40px;
  }
  .card {
    position: relative;
    width: 540px; height: 309px;
    background: var(--card-dark);
    overflow: hidden;
    box-shadow: 0 10px 28px rgba(0,0,0,0.28);
  }
  /* Front */
  .front .faint-mark {
    position: absolute; right: 70px; top: -40px;
    width: 220px; height: 220px; border-radius: 50%;
    background: var(--card-dark-soft);
  }
  .brand {
    position: absolute; left: 34px; top: 56px;
    display: flex; align-items: center; gap: 14px;
  }
  .brand-dot {
    width: 40px; height: 40px; border-radius: 50%;
    background: var(--brand-blue);
  }
  .brand-name {
    font-family: "Montserrat", Arial, sans-serif;
    font-weight: 700; font-size: 34px; letter-spacing: 0.5px;
    color: var(--brand-blue);
  }
  .person { position: absolute; left: 36px; top: 138px; }
  .person-name {
    font-family: "Montserrat", Arial, sans-serif;
    font-weight: 700; font-size: 22px; letter-spacing: 1px;
    color: var(--brand-blue);
  }
  .person-role { font-size: 13px; color: var(--text-light); margin-top: 2px; }
  .contact {
    position: absolute; left: 36px; top: 208px;
    list-style: none; display: flex; flex-direction: column; gap: 5px;
  }
  .contact li {
    display: flex; align-items: center; gap: 9px;
    font-size: 13px; color: var(--text-light);
  }
  .contact svg { width: 12px; height: 12px; flex: none; }
  .address {
    position: absolute; right: 30px; bottom: 36px;
    font-size: 12px; line-height: 1.5; color: var(--text-light); text-align: right;
  }
  .edge-band {
    position: absolute; left: 0; right: 0; bottom: 0; height: 8px;
    display: flex;
  }
  .edge-band .blue { flex: 0 0 46%; background: var(--brand-blue); }
  .edge-band .white { flex: 1; background: var(--paper-white); }
  /* Back */
  .back .pattern-field {
    position: absolute; inset: 0;
    background: linear-gradient(135deg, #1b1b1c 0%, #2a2a2b 55%, #4a4a4b 100%);
  }
  .back .brand { left: auto; right: 40px; top: auto; bottom: 60px; }
</style>
</head>
<body>
<main class="stage">
  <section class="card front" aria-label="Business card front">
    <div class="faint-mark" aria-hidden="true"></div>
    <div class="brand">
      <span class="brand-dot" aria-hidden="true"></span>
      <span class="brand-name">LUMA: Dry Eye</span>
    </div>
    <div class="person">
      <p class="person-name">DORIAN HALE</p>
      <p class="person-role">CEO/Founder</p>
    </div>
    <ul class="contact">
      <li>
        <svg viewBox="0 0 12 12" aria-hidden="true"><path d="M2.5 1l2 2.2-1 1.3c.7 1.5 1.8 2.6 3.3 3.3l1.3-1 2.2 2-1.2 1.7C5 10 2 7 .8 2.3L2.5 1z" fill="var(--brand-blue)"/></svg>
        (555) 210 4417
      </li>
      <li>
        <svg viewBox="0 0 12 12" aria-hidden="true"><rect x="0.5" y="2" width="11" height="8" fill="var(--brand-blue)"/><path d="M0.5 2l5.5 4.5L11.5 2" stroke="var(--card-dark)" stroke-width="1" fill="none"/></svg>
        info@lumadryeye.com
      </li>
      <li>
        <svg viewBox="0 0 12 12" aria-hidden="true"><circle cx="6" cy="6" r="5.5" fill="var(--brand-blue)"/><path d="M.5 6h11M6 .5v11M2 3h8M2 9h8" stroke="var(--card-dark)" stroke-width="0.7"/></svg>
        www.lumadryeye.com
      </li>
    </ul>
    <p class="address">P.O. Box 7310 Harbour Road<br>Region Name QC 4127</p>
    <div class="edge-band" aria-hidden="true"><span class="blue"></span><span class="white"></span></div>
  </section>

  <section class="card back" aria-label="Business card back">
    <div class="pattern-field" role="img" aria-label="Repeating tone-on-tone brand pattern across the dark card back"></div>
    <div class="brand">
      <span class="brand-dot" aria-hidden="true"></span>
      <span class="brand-name">LUMA: Dry Eye</span>
    </div>
  </section>
</main>
</body>
</html>
```